School Poster

Design so that these can be placed in classrooms across the school.

Attached is another design we have had done. Use a similar theme.

Consider using themes from https://tolvanehs.qx.edu.au/

please edit Binder1 doc.

Target Market(s)

Students and teachers

```html
<!DOCTYPE html>
<html lang="en">
<head>
<meta charset="utf-8">
<title>Before You Ask the Teacher – Tolvane</title>
<link rel="stylesheet" href="https://fonts.googleapis.com/css2?family=Poppins:wght@300;400;700;800;900&family=Roboto:wght@400&display=swap">
<style>
:root{
  --backdrop:#d7d8d7;
  --blue:#2f4a93;
  --yellow:#f3e256;
  --ink:#2b2b2b;
  --panel:#eeeeee;
  --white:#ffffff;
}
*{box-sizing:border-box;margin:0;padding:0}
html,body{width:1030px;height:1200px;overflow:hidden;background:var(--backdrop)}
body{position:relative;font-family:"Poppins",sans-serif;color:var(--ink)}
.poster{position:absolute;left:184px;top:132px;width:662px;height:936px;background:var(--white);overflow:hidden}
.header{position:absolute;left:0;top:0;width:662px;height:203px;background:var(--blue)}
.header__band{position:absolute;left:0;top:127px;width:662px;height:41px;background:var(--yellow)}
.header__title{position:absolute;left:33px;top:28px;font-weight:800;font-size:52px;line-height:44px;color:var(--white);letter-spacing:.2px}
.header__tagline{position:absolute;left:33px;top:126px;font-family:"Roboto",sans-serif;font-weight:400;font-size:37px;line-height:42px;color:var(--ink)}
.school-name{position:absolute;left:512px;top:58px;width:126px;display:flex;flex-direction:column;align-items:center;gap:8px}
.school-name__dot{width:14px;height:14px;border-radius:50%;background:var(--yellow)}
.school-name__text{font-weight:800;font-size:22px;color:var(--white);letter-spacing:.5px}

.step{position:absolute;top:233px;width:191px;height:579px;border:2.5px solid var(--blue);border-radius:12px;background:var(--white)}
.step--think{left:32px}
.step--check{left:235px}
.step--ask{left:438px}
.step__number{position:absolute;left:50%;top:-18px;transform:translateX(-50%);width:36px;height:36px;border-radius:50%;background:var(--blue);color:var(--white);font-weight:800;font-size:24px;line-height:36px;text-align:center;box-shadow:0 0 0 8px var(--white)}
.step__icon{position:absolute;left:50%;top:31px;transform:translateX(-50%);width:130px;height:122px}
.step__title{position:absolute;left:0;right:0;top:190px;height:80px;display:flex;align-items:center;justify-content:center;text-align:center;font-weight:900;font-size:27px;line-height:26px;color:var(--blue);text-transform:uppercase}
.step__lead{position:absolute;left:0;right:0;top:268px;height:63px;background:var(--yellow);display:flex;align-items:center;justify-content:center;text-align:center;font-weight:700;font-size:16.5px;line-height:18px;color:var(--ink);padding:0 4px}
.step__body{position:absolute;left:0;right:0;top:331px;bottom:0;background:var(--panel);border-radius:0 0 10px 10px;padding:11px 4px 0 18px}
.step__list{list-style:none}
.step__list li{position:relative;padding-left:17px;font-weight:300;font-size:14.4px;line-height:19.7px;margin-bottom:5.3px;color:var(--ink);letter-spacing:-.1px}
.step__list li::before{content:"";position:absolute;left:1px;top:7px;width:6px;height:6px;border-radius:50%;background:var(--ink)}
.step--check .step__list li::before{background:var(--blue)}
.step__closing{font-weight:700;font-size:14px;line-height:20px;color:var(--ink);margin-top:0;margin-left:-2px}
.step__value{position:absolute;left:50%;bottom:-19px;transform:translateX(-50%);height:37px;padding:0 8px;border-radius:12px;background:var(--blue);color:var(--white);font-weight:900;font-size:20px;line-height:37px;white-space:nowrap;text-transform:uppercase;text-align:center}
.step--think .step__value,.step--check .step__value{width:157px}
.step--ask .step__value{width:168px}

.references{position:absolute;left:0;top:846px;width:662px;height:90px;background:var(--yellow);padding:12px 0 0 75px;font-size:9.4px;line-height:11.5px;color:var(--ink);font-weight:400}
.references__heading{font-weight:700;font-size:9.5px;margin-bottom:4px}
.references__item{margin-bottom:3px}
</style>
</head>
<body>
<main class="poster">
  <header class="header">
    <div class="header__band"></div>
    <h1 class="header__title">BEFORE YOU ASK<br>THE TEACHER...</h1>
    <p class="header__tagline">TRY THESE STEPS FIRST!</p>
    <div class="school-name" aria-label="Tolvane">
      <span class="school-name__dot"></span>
      <span class="school-name__text">TOLVANE</span>
    </div>
  </header>

  <section class="step step--think">
    <div class="step__number">1</div>
    <svg class="step__icon" viewBox="0 0 130 122" aria-hidden="true">
      <path d="M66 8 C40 2 18 18 16 42 L16 52 L6 66 L14 70 L12 84 C14 92 22 92 30 92 L30 104 L36 110 L86 108 L86 118 L30 118" fill="none" stroke="var(--blue)" stroke-width="4.5" stroke-linecap="round" stroke-linejoin="round"/>
      <g fill="none" stroke="var(--yellow)" stroke-width="4.5" stroke-linecap="round">
        <path d="M82 66 C82 58 72 54 72 40 A24 24 0 0 1 120 40 C120 54 110 58 110 66 Z"/>
        <line x1="82" y1="74" x2="110" y2="74"/>
        <line x1="86" y1="82" x2="106" y2="82"/>
        <circle cx="96" cy="40" r="9"/>
        <line x1="96" y1="6" x2="96" y2="2"/>
        <line x1="66" y1="40" x2="62" y2="40"/>
        <line x1="126" y1="40" x2="130" y2="40"/>
        <line x1="73" y1="18" x2="70" y2="15"/>
        <line x1="119" y1="18" x2="122" y2="15"/>
        <line x1="73" y1="62" x2="70" y2="65"/>
        <line x1="119" y1="62" x2="122" y2="65"/>
      </g>
    </svg>
    <h2 class="step__title">Think<br>First</h2>
    <p class="step__lead">Don't give up<br>straight away.</p>
    <div class="step__body">
      <ul class="step__list">
        <li>Read the question carefully.</li>
        <li>Identify what you already know.</li>
        <li>Try a strategy you've used before.</li>
        <li>Give yourself thinking time.</li>
      </ul>
    </div>
    <div class="step__value">We Believe</div>
  </section>

  <section class="step step--check">
    <div class="step__number">2</div>
    <svg class="step__icon" viewBox="0 0 130 122" aria-hidden="true">
      <rect x="20" y="14" width="88" height="104" rx="10" fill="none" stroke="var(--blue)" stroke-width="6"/>
      <path d="M46 14 L46 6 Q46 2 50 2 L78 2 Q82 2 82 6 L82 14 L82 20 L46 20 Z" fill="var(--white)" stroke="var(--blue)" stroke-width="5" stroke-linejoin="round"/>
      <g stroke="var(--blue)" stroke-width="6" stroke-linecap="round">
        <line x1="36" y1="46" x2="76" y2="46"/>
        <line x1="36" y1="70" x2="76" y2="70"/>
        <line x1="36" y1="94" x2="76" y2="94"/>
      </g>
      <g fill="none" stroke="var(--yellow)" stroke-width="5" stroke-linecap="round" stroke-linejoin="round">
        <path d="M84 46 L89 51 L98 40"/>
        <path d="M84 70 L89 75 L98 64"/>
        <path d="M84 94 L89 99 L98 88"/>
      </g>
    </svg>
    <h2 class="step__title">Check<br>Your<br>Supports</h2>
    <p class="step__lead">Before asking for<br>help, check:</p>
    <div class="step__body">
      <ul class="step__list">
        <li>Learning goal and success criteria.</li>
        <li>Worked examples.</li>
        <li>Class notes.</li>
        <li>Classroom displays.</li>
        <li>Lumi resources.</li>
        <li>Task sheet and instructions.</li>
      </ul>
    </div>
    <div class="step__value">We Strive</div>
  </section>

  <section class="step step--ask">
    <div class="step__number">3</div>
    <svg class="step__icon" viewBox="0 0 160 122" style="width:160px" aria-hidden="true">
      <g fill="none" stroke="var(--yellow)" stroke-width="5" stroke-linejoin="round" stroke-linecap="round">
        <circle cx="30" cy="34" r="17"/>
        <path d="M38 49 L44 60 L45 47"/>
        <circle cx="80" cy="24" r="18"/>
        <path d="M73 41 L80 51 L87 41"/>
        <circle cx="130" cy="34" r="17"/>
        <path d="M122 49 L116 60 L115 47"/>
      </g>
      <g fill="var(--blue)">
        <circle cx="46" cy="74" r="11"/>
        <circle cx="80" cy="74" r="11"/>
        <circle cx="114" cy="74" r="11"/>
        <path d="M20 114 Q22 90 46 88 Q62 90 66 102 L62 114 Z"/>
        <path d="M98 114 Q98 102 94 102 Q98 90 114 88 Q138 90 140 114 Z"/>
        <path d="M54 114 Q56 90 80 88 Q104 90 106 114 Z"/>
      </g>
    </svg>
    <h2 class="step__title">Ask 3<br>Before Me</h2>
    <p class="step__lead">Ask three sources<br>before asking<br>the teacher:</p>
    <div class="step__body">
      <ul class="step__list">
        <li>A person (partner or neighbour)</li>
        <li>A place (notes, display, Lumi)</li>
        <li>A resource (worked example, task sheet)</li>
      </ul>
      <p class="step__closing">Then ask the teacher if you still need help.</p>
    </div>
    <div class="step__value">We Achieve</div>
  </section>

  <footer class="references">
    <p class="references__heading">References</p>
    <p class="references__item">Marlowe, J. (2025). Why Students Don't Ask for Help – And How to Change That. Downloaded 24/04/2026<br>from:https://www.learnwell.org/article/asking-for-help/</p>
    <p class="references__item">CERL. (2024). Supporting Self-Regulated Learning. Downloaded 24/04/2026<br>from:https://www.cerlresearch.org/files/2024-02/supporting-self-regulated-learning.pdf</p>
  </footer>
</main>
</body>
</html>
```